Corporate Business Card

Very professional, Modern, Not to busy, include phone address email, website
(253) 555-0174, 61807 19th Street N, Kent, WA 98517, marcus@kestrelbayholding.com, brelvanindustries.com

Target Market(s)

Manufacturing

Industry/Entity Type

Aero, machining, manufacturing, Off road racing

Contact Information for Business Card

Phone, address email, website

```html
<!DOCTYPE html>
<html lang="en">
<head>
<meta charset="utf-8">
<title>Brelvan Industries – Business Card</title>
<link href="https://fonts.googleapis.com/css2?family=Arimo:wght@400;700&display=swap" rel="stylesheet">
<style>
  :root {
    --navy: #13306a;
    --navy-soft: #1d4183;
    --red: #d3252f;
    --white: #f6f6f8;
    --ink: #ffffff;
    --page: #2a2b2e;
  }
  * { margin: 0; padding: 0; box-sizing: border-box; }
  html, body {
    width: 1200px; height: 874px; overflow: hidden;
    background: var(--page);
    font-family: "Arimo", Arial, sans-serif;
  }
  .stage {
    width: 1200px; height: 874px;
    display: flex; flex-direction: column; align-items: center; justify-content: center;
    gap: 40px;
  }
  .card {
    position: relative;
    width: 620px; height: 354px;
    overflow: hidden;
    box-shadow: 0 10px 30px rgba(0,0,0,.45);
  }
  /* back of card */
  .card-back { background: var(--navy); }
  .card-back .wordmark {
    position: absolute; left: 0; right: 0; top: 50%;
    transform: translateY(-50%);
    text-align: center;
    color: var(--navy-soft);
    font-weight: 700;
  }
  .card-back .wordmark .name { display: block; font-size: 92px; letter-spacing: 2px; line-height: 1; }
  .card-back .wordmark .sub { display: block; font-size: 30px; margin-top: 8px; letter-spacing: 1px; }
  /* front of card */
  .card-front { background: var(--white); }
  .card-front .panel { position: absolute; inset: 0; }
  .brand {
    position: absolute; left: 34px; top: 142px;
    width: 230px; text-align: center;
    color: var(--navy); font-weight: 700;
  }
  .brand .name { display: block; font-size: 40px; letter-spacing: 1px; line-height: 1; }
  .brand .sub { display: block; font-size: 16px; margin-top: 6px; }
  .contact {
    position: absolute; left: 322px; top: 78px;
    color: var(--ink);
  }
  .contact .person { font-size: 22px; font-weight: 700; text-transform: uppercase; letter-spacing: .5px; }
  .contact .role { font-size: 13px; margin-top: 2px; }
  .contact .address { font-size: 14px; line-height: 1.35; margin-top: 16px; }
  .contact .lines { list-style: none; margin-top: 12px; font-size: 14px; line-height: 1.5; }
  .contact .lines li { display: flex; align-items: center; gap: 8px; }
  .contact .lines svg { width: 12px; height: 12px; flex: none; fill: var(--ink); }
</style>
</head>
<body>
<main class="stage">
  <section class="card card-back" aria-label="Card back">
    <div class="wordmark">
      <span class="name">BRELVAN</span>
      <span class="sub">Industries</span>
    </div>
  </section>

  <section class="card card-front" aria-label="Card front">
    <svg class="panel" viewBox="0 0 620 354" preserveAspectRatio="none" aria-hidden="true">
      <polygon points="300,0 620,0 620,354 266,354" fill="#13306a"/>
      <polygon points="296,0 301,0 267,354 262,354" fill="#d3252f"/>
    </svg>
    <div class="brand">
      <span class="name">BRELVAN</span>
      <span class="sub">Industries</span>
    </div>
    <div class="contact">
      <p class="person">Daniel Hartley</p>
      <p class="role">Managing Director</p>
      <p class="address">61807 19th Street N<br>Kent, WA 98517</p>
      <ul class="lines">
        <li><svg viewBox="0 0 24 24"><path d="M6.6 10.8a15.1 15.1 0 0 0 6.6 6.6l2.2-2.2a1 1 0 0 1 1-.25 11.4 11.4 0 0 0 3.6.57 1 1 0 0 1 1 1V20a1 1 0 0 1-1 1A17 17 0 0 1 3 4a1 1 0 0 1 1-1h3.5a1 1 0 0 1 1 1c0 1.25.2 2.45.57 3.57a1 1 0 0 1-.25 1z"/></svg>(253) 555-0174</li>
        <li><svg viewBox="0 0 24 24"><path d="M2 5h20v14H2z M2 5l10 8 10-8" fill="none" stroke="#fff" stroke-width="2"/></svg>marcus@kestrelbayholding.com</li>
        <li><svg viewBox="0 0 24 24"><circle cx="12" cy="12" r="9" fill="none" stroke="#fff" stroke-width="2"/><path d="M3 12h18M12 3c3 3 3 15 0 18M12 3c-3 3-3 15 0 18" fill="none" stroke="#fff" stroke-width="1.6"/></svg>brelvanindustries.com</li>
      </ul>
    </div>
  </section>
</main>
</body>
</html>
```